IT company requires website redesign

I have an old boring website that I want to update - www.tvkb-example.net
I am a growing IT company beginning to look after more healthcare professionals such as medical and dental practices so a more professional look is required

Blue and orange are the company colours. See one of our local competitors for your reference and ideas - https://www.plinth-halvard.example.au

Target Market(s)

Medical, dental, professional, solicitors etc

Industry/Entity Type

It Support

Number of Pages Required

5+ page

Colors

Designer to choose colors to be used in the design.

Requirements
Must have
• Classy feel, simple with the 'less is more' approach
• On support page, links to support items, a couple more to come
• Reference to our technology partners
• Easy to read
Nice to have
• Company colours are blue with a little orange but I willing to consider new web colour schemes
• leave the rest to you

```html
<!DOCTYPE html>
<html lang="en">
<head>
<meta charset="utf-8">
<title>Meridian Systems – IT Support</title>
<link rel="stylesheet" href="https://fonts.googleapis.com/css2?family=Montserrat:wght@400;500;600&family=Roboto:wght@300;400;500&display=swap">
<style>
:root{
  --blue:#0b92dc;
  --blue-deep:#0676c4;
  --blue-light:#19a8ec;
  --navy:#0e2a50;
  --navy-card:#13325d;
  --orange:#f7a21b;
  --ink:#2d2d2d;
  --muted:#8a8f96;
  --panel:#f1f3f6;
  --line:#e3e6ea;
  --white:#ffffff;
}
*{box-sizing:border-box;margin:0;padding:0}
html,body{width:1200px;height:3066px;overflow:hidden}
body{position:relative;font-family:"Roboto",Arial,sans-serif;color:var(--ink);background:var(--white)}
.abs{position:absolute}
h1,h2,h3,h4,.brand{font-family:"Montserrat",Arial,sans-serif;font-weight:500}
a{color:inherit;text-decoration:none}
.btn{position:absolute;display:flex;align-items:center;justify-content:center;font-size:12px;border-radius:2px}
.btn-orange{background:var(--orange);color:var(--white)}
.btn-blue{background:var(--blue-deep);color:var(--white)}
.btn-white{background:var(--white);color:var(--ink)}

/* hero */
.hero{left:0;top:0;width:1200px;height:420px;background:linear-gradient(180deg,var(--blue-deep) 0%,var(--blue) 45%,var(--blue-light) 100%)}
.topbar{left:0;top:0;width:1200px;height:57px;background:rgba(0,70,140,.25)}
.brand{position:absolute;left:233px;top:17px;color:var(--white);font-size:15px;font-weight:600;display:flex;align-items:center;gap:7px}
.nav{left:533px;top:21px;display:flex;gap:22px;font-size:11.5px;color:rgba(255,255,255,.85)}
.nav .on{color:var(--white);border-bottom:2px solid var(--white);padding-bottom:14px}
.social{display:flex;gap:10px}
.social i{width:9px;height:9px;border-radius:50%;background:currentColor;display:block}
.hero-title{left:233px;top:134px;width:400px;color:var(--white);font-size:23px;line-height:31px;font-weight:500}
.hero-tag{left:233px;top:248px;width:340px;color:var(--white);font-size:14px;line-height:21px}
.hero-art{left:603px;top:78px;width:370px;height:326px;border-radius:6px;background:linear-gradient(150deg,rgba(255,255,255,.35),rgba(205,230,250,.85) 60%,rgba(240,248,255,.9))}

/* welcome card */
.intro{left:233px;top:405px;width:732px;height:353px;background:var(--white);box-shadow:0 6px 24px rgba(0,0,0,.12);display:flex}
.intro .col{padding:26px 42px;font-size:10px;line-height:15.5px;color:#555}
.intro .left{width:435px}
.intro .right{width:297px;background:var(--panel);padding:26px 30px}
.intro h3{font-size:14px;color:var(--ink);font-weight:400}
.intro h2{font-size:22px;color:var(--ink);font-weight:400;margin-bottom:22px}
.intro p{margin-bottom:14px}
.ticks{list-style:none}
.ticks li{position:relative;padding-left:22px;margin-bottom:6px}
.ticks li:before{content:"";position:absolute;left:4px;top:3px;width:7px;height:4px;border-left:2px solid var(--blue);border-bottom:2px solid var(--blue);transform:rotate(-45deg)}

/* headings */
.sec-title{left:0;width:1200px;text-align:center;font-size:23px;font-weight:400}
.sec-lead{left:320px;width:560px;text-align:center;font-size:10px;line-height:17px;color:#666}

/* services */
.service{width:170px;text-align:center}
.service .ico{width:57px;height:57px;border-radius:50%;margin:0 auto 12px;display:flex;align-items:center;justify-content:center}
.service h4{font-family:"Montserrat",Arial,sans-serif;font-weight:400;font-size:13px;margin-bottom:8px}
.service p{font-size:10px;line-height:16px;color:var(--muted);padding:0 8px}

/* testimonials */
.wave{left:0;top:1400px;width:1200px;height:660px}
.quote{top:1631px;width:346px;height:284px;background:var(--navy-card);padding:26px 26px;color:rgba(255,255,255,.78);font-size:10px;line-height:16.5px}
.quote .mark{font-family:"Montserrat",Arial,sans-serif;font-size:54px;line-height:40px;color:var(--white);font-weight:600}
.quote .who{margin-top:12px;color:var(--white)}
.quote .who b{color:var(--blue-light);font-weight:400}
.dots{left:588px;top:1949px;display:flex;gap:4px}
.dots i{width:5px;height:5px;border-radius:50%;border:1px solid rgba(255,255,255,.7);display:block}
.dots i.on{background:var(--white)}

/* partners */
.partners{left:253px;top:2226px;width:692px;display:grid;grid-template-columns:repeat(5,126px);gap:12px 15px}
.partner{height:58px;border:1px solid var(--line);border-radius:3px;display:flex;align-items:center;justify-content:center}
.partner span{display:block;width:64px;height:16px;border-radius:3px;background:#d9dde3}

/* newsletter */
.news-wave{left:0;top:2480px;width:1200px;height:304px}
.news-title{left:0;top:2600px;width:1200px;text-align:center;color:var(--white);font-size:22px;font-weight:400}
.news-lead{left:370px;top:2644px;width:460px;text-align:center;color:var(--white);font-size:10px;line-height:16px}
.subscribe{left:462px;top:2700px;width:276px;height:32px;display:flex;border:1px solid rgba(255,255,255,.8)}
.subscribe .field{flex:1;color:rgba(255,255,255,.9);font-size:10px;padding:10px 10px}
.subscribe .go{width:96px;background:var(--white);color:var(--blue);font-size:12px;display:flex;align-items:center;justify-content:center}

/* footer */
.footer{left:0;top:2780px;width:1200px;height:204px;background:var(--blue)}
.fcol{top:2822px;color:var(--white);font-size:10.5px;line-height:18.5px}
.fcol h4{font-size:11.5px;font-weight:600;margin-bottom:6px;line-height:14px}
.fcol a{display:block;color:rgba(255,255,255,.85)}
.fcol a.on{color:var(--white);font-weight:500}
.bottom{left:0;top:2984px;width:1200px;height:82px;background:var(--white)}
.bottom .brand{color:var(--blue-deep);top:33px;font-size:13px}
.copy{left:0;top:3012px;width:1200px;text-align:center;font-size:9.5px;color:#888}
</style>
</head>
<body>

<!-- hero -->
<section class="abs hero"></section>
<header class="abs topbar">
  <a class="brand" href="#">Meridian Systems</a>
  <nav class="abs nav">
    <a class="on" href="#">Home</a><a href="#">Our Services</a><a href="#">About</a><a href="#">Team</a><a href="#">Contact</a><a href="#">Support</a>
  </nav>
  <div class="abs social" style="left:914px;top:24px;color:#fff" aria-label="Social links"><i></i><i></i><i></i></div>
</header>
<h1 class="abs hero-title">We’re Meridian Systems<br>an Information Technology<br>Company!</h1>
<p class="abs hero-tag">A Better Tomorrow, Through Intelligent use of<br>Technology Today!</p>
<a class="btn btn-white" href="#" style="left:233px;top:312px;width:114px;height:32px">Get In Touch</a>
<div class="abs hero-art" role="img" aria-label="Isometric illustration of people working around a large laptop with floating app screens"></div>

<!-- intro card -->
<section class="abs intro">
  <div class="col left">
    <h3>Welcome to</h3>
    <h2>Meridian Systems</h2>
    <p>Welcome to Meridian Systems where we believe that a better tomorrow, starts through intelligent use of technology today!</p>
    <p>Meridian Systems is a valued added Information technology company supplying and implementing hardware and software that are complemented by the provision of associated support services and solutions.</p>
    <p>We ensure that the risks associated with the deployment of new technologies are reduced, while providing a competitive total cost of IT ownership that yields a compelling return on investment.</p>
  </div>
  <div class="col right">
    <h3>How we</h3>
    <h2>can save you $$$</h2>
    <p>We pride ourselves in offering only the best solutions, with our diverse skill set in areas including:</p>
    <ul class="ticks">
      <li>Medical Software including ClinicDesk, PracLedger and CareSuite. We can also assist with eHIP compliance.</li>
      <li>Legal packages including LexFile</li>
      <li>Terminal Services/RDP connections</li>
      <li>Mailhub Server</li>
    </ul>
  </div>
</section>
<a class="btn btn-orange" href="#" style="left:277px;top:688px;width:110px;height:32px">Learn More</a>
<a class="btn btn-blue" href="#" style="left:723px;top:688px;width:110px;height:32px">Learn More</a>

<!-- services -->
<h2 class="abs sec-title" style="top:836px">Our Services</h2>
<p class="abs sec-lead" style="top:880px">Lorem ipsum dolor sit amet, consectetur adipiscing elit. Mauris bibendum sollicitudin orci, efficitur aliquam libero aliquam non. Nullam faucibus, quam non blandit cursus, nulla nisi porta nisl, ac rhoncus purus nisl eget arcu.</p>

<div class="abs service" style="left:226px;top:952px"><div class="ico" style="background:#7a5bd6"><svg width="22" height="22"><rect x="3" y="3" width="16" height="12" fill="none" stroke="#fff" stroke-width="2"/><rect x="7" y="17" width="8" height="2" fill="#fff"/></svg></div><h4>Software</h4><p>Meridian Systems has the tools, capabilities and expertise to guide any organisation with their software requirements</p></div>
<div class="abs service" style="left:416px;top:952px"><div class="ico" style="background:#ee7f22"><svg width="22" height="22"><rect x="3" y="4" width="16" height="11" fill="none" stroke="#fff" stroke-width="2"/><path d="M8 19h6" stroke="#fff" stroke-width="2"/></svg></div><h4>Products</h4><p>Meridian Systems has the tools, capabilities and expertise to guide any organisation with their software requirements</p></div>
<div class="abs service" style="left:610px;top:952px"><div class="ico" style="background:#27c6c6"><svg width="22" height="22"><rect x="3" y="3" width="16" height="16" fill="none" stroke="#fff" stroke-width="2"/><path d="M11 3v16M3 11h16" stroke="#fff" stroke-width="2"/></svg></div><h4>Solutions</h4><p>Meridian Systems has the tools, capabilities and expertise to guide any organisation with their software requirements</p></div>
<div class="abs service" style="left:804px;top:952px"><div class="ico" style="background:#fbc43c"><svg width="22" height="22"><path d="M3 8l8-5 8 5z" fill="#fff"/><path d="M5 10v7M9 10v7M13 10v7M17 10v7M3 19h16" stroke="#fff" stroke-width="2"/></svg></div><h4>Finance – Flexi Rent</h4><p>Meridian Systems has the tools, capabilities and expertise to guide any organisation with their software requirements</p></div>

<div class="abs service" style="left:226px;top:1150px"><div class="ico" style="background:#6cc04a"><svg width="22" height="22"><rect x="3" y="4" width="16" height="12" fill="none" stroke="#fff" stroke-width="2"/><path d="M8 9l-2 2 2 2M14 9l2 2-2 2" stroke="#fff" stroke-width="1.5" fill="none"/></svg></div><h4>Programming</h4><p>Meridian Systems has the tools, capabilities and expertise to guide any organisation with their software requirements</p></div>
<div class="abs service" style="left:416px;top:1150px"><div class="ico" style="background:#f2545b"><svg width="22" height="22"><rect x="6" y="3" width="10" height="14" fill="none" stroke="#fff" stroke-width="2"/><rect x="4" y="6" width="10" height="14" fill="#f2545b" stroke="#fff" stroke-width="2"/></svg></div><h4>Copiers</h4><p>Meridian Systems has the tools, capabilities and expertise to guide any organisation with their software requirements</p></div>
<div class="abs service" style="left:610px;top:1150px"><div class="ico" style="background:#1aa3e8"><svg width="22" height="22"><rect x="6" y="3" width="10" height="5" fill="#fff"/><rect x="3" y="8" width="16" height="8" fill="none" stroke="#fff" stroke-width="2"/><rect x="6" y="14" width="10" height="5" fill="#fff"/></svg></div><h4>Printers &amp; Scanners</h4><p>Meridian Systems has the tools, capabilities and expertise to guide any organisation with their software requirements</p></div>
<div class="abs service" style="left:804px;top:1150px"><div class="ico" style="background:#5a1fb8"><svg width="22" height="22"><path d="M3 10l8-6 8 6" fill="none" stroke="#fff" stroke-width="2"/><rect x="6" y="10" width="10" height="9" fill="#fff"/></svg></div><h4>Web Hosting and Design</h4><p>Meridian Systems has the tools, capabilities and expertise to guide any organisation with their software requirements</p></div>

<a class="btn btn-orange" href="#" style="left:544px;top:1353px;width:110px;height:33px">Read More</a>

<!-- testimonials -->
<svg class="abs wave" viewBox="0 0 1200 660" preserveAspectRatio="none" aria-hidden="true">
  <defs><linearGradient id="navyGrad" x1="0" y1="0" x2="1" y2="1"><stop offset="0" stop-color="#0c2446"/><stop offset="1" stop-color="#163b6e"/></linearGradient></defs>
  <path d="M0 10 C300 90 800 110 1200 0 L1200 540 C900 640 400 560 0 470 Z" fill="#b8c0cc"/>
  <path d="M0 10 C300 80 800 100 1200 30 L1200 520 C900 610 400 540 0 450 Z" fill="#7d8aa0"/>
  <path d="M0 10 C300 70 800 90 1200 60 L1200 500 C900 580 400 520 0 430 Z" fill="url(#navyGrad)"/>
</svg>
<h2 class="abs sec-title" style="top:1522px;color:#fff">What our client speaks about us</h2>
<p class="abs sec-lead" style="top:1567px;color:rgba(255,255,255,.7)">Lorem ipsum dolor sit amet, consectetur adipiscing elit. Mauris bibendum sollicitudin orci, efficitur aliquam libero aliquam non. Nullam faucibus, quam non blandit cursus, nulla nisi porta nisl, ac rhoncus purus nisl eget arcu.</p>

<article class="abs quote" style="left:233px">
  <div class="mark">“</div>
  <p>Meridian Systems have been our IT support company for over 10 years. So why do we stick with them? Because they are awesome!! Sam and his staff are consistently able to solve our many and varied problems. Whether we phone about server functionality, email capacity, software issues or IT security, Sam and the team are always able to provide a quick and efficient response, leaving us to get on with our business. Reliable, knowledgeable, cost effective – Meridian Systems are an asset to our company and I cannot recommend them highly enough.</p>
  <p class="who"><b>Harriet Vale</b> - Administration Manager</p>
</article>
<article class="abs quote" style="left:619px">
  <div class="mark">“</div>
  <p>Meridian Systems have saved us time, money and stress by implementing technology solutions for our business computer requirements. Problems we have experienced with any of our existing software or hardware applications have been dealt with in a professional, speedy and pleasant manner, whether attended by Sam or by any one of his skilled team. We have been impressed at the professional integrity of this team as a whole and would not hesitate to recommend them to business associates.</p>
  <p class="who"><b>Neil and Ruth Ambers</b></p>
</article>
<div class="abs dots"><i class="on"></i><i></i><i></i></div>

<!-- partners -->
<h2 class="abs sec-title" style="top:2110px">Some of our Partners</h2>
<p class="abs sec-lead" style="top:2155px;left:370px;width:460px">We partner with only the best companies around the world to offer our clients the BEST in Hardware and Software solutions</p>
<div class="abs partners" aria-label="Technology partners">
  <div class="partner"><span></span></div><div class="partner"><span></span></div><div class="partner"><span></span></div><div class="partner"><span></span></div><div class="partner"><span></span></div>
  <div class="partner"><span></span></div><div class="partner"><span></span></div><div class="partner"><span></span></div><div class="partner"><span></span></div><div class="partner"><span></span></div>
</div>
<a class="btn btn-blue" href="#" style="left:546px;top:2393px;width:110px;height:33px">Get In Touch</a>

<!-- newsletter -->
<svg class="abs news-wave" viewBox="0 0 1200 304" preserveAspectRatio="none" aria-hidden="true">
  <defs><linearGradient id="newsGrad" x1="0" y1="0" x2="0" y2="1"><stop offset="0" stop-color="#0a86d0"/><stop offset="1" stop-color="#0b92dc"/></linearGradient></defs>
  <path d="M0 70 C300 -20 700 0 1200 80 L1200 304 L0 304 Z" fill="#cfe6f6"/>
  <path d="M0 80 C400 10 800 90 1200 40 L1200 304 L0 304 Z" fill="#7cc1ea"/>
  <path d="M0 110 C350 40 800 50 1200 110 L1200 304 L0 304 Z" fill="url(#newsGrad)"/>
</svg>
<h2 class="abs news-title">Newsletter Subscription</h2>
<p class="abs news-lead">Lorem ipsum dolor sit amet, consectetur adipiscing elit. Mauris bibendum sollicitudin orci, efficitur aliquam libero aliquam non. Nullam faucibus, quam non blandit cursus.</p>
<form class="abs subscribe"><div class="field">Enter your email address...</div><div class="go">Get In Touch</div></form>

<!-- footer -->
<footer class="abs footer"></footer>
<div class="abs fcol" style="left:233px"><h4>Links</h4><a class="on" href="#">Home</a><a href="#">About</a><a href="#">Team</a><a href="#">Contact</a><a href="#">Support</a></div>
<div class="abs fcol" style="left:366px"><h4>Our Services</h4><a href="#">Software</a><a href="#">Products</a><a href="#">Solutions</a><a href="#">Finance – Flexi Rent</a><a href="#">Programming</a></div>
<div class="abs fcol" style="left:495px"><h4>&nbsp;</h4><a href="#">Copiers</a><a href="#">Printers &amp; Scanners</a><a href="#">Web Hosting and Design</a></div>
<div class="abs fcol" style="left:705px"><h4>Support</h4><a href="#">Contact</a><a href="#">FAQ</a><a href="#">Service Status</a></div>
<div class="abs fcol" style="left:883px"><h4>Legal</h4><a href="#">Terms</a><a href="#">Privacy</a></div>

<div class="abs bottom">
  <a class="brand" href="#" style="left:233px">Meridian Systems</a>
</div>
<p class="abs copy">Copyright © 2018, Meridian Systems</p>
<div class="abs social" style="left:912px;top:3013px;color:var(--blue)" aria-label="Social links"><i></i><i></i><i></i></div>

</body>
</html>
```